My dynamic new collection of short plays needs an eye catching web-based ad!

I am buying ad space on a theater magazine's website with these specs for a new book. The ad will run for a few months. I have the book cover - which will be the main image, but need the ad designed with quotes and the publisher's logo. Here are the specs:
230 pixels wide x 250 pixels high
72 dpi

Target Market(s)

Theater artists and theater educators

Industry/Entity Type

Theater / Education

Font styles to use
Sans Serif
Other font styles liked:
• Please use fonts that match the book cover. I'm including an ad that is currently on the website where I will be advertising. It is not the size that I'm going for, but it contains the elements that I want. I'm also including an image of the logo of the publisher, and I have other versions of this logo (other formats / larger size) that I can deliver if needed.

Requirements
Must have
• Simple compelling image with a quote from the book and a link to the publisher website. A compelling quote (or two) from the book jacket. The name and logo of the publisher.
Nice to have
• Some eye catching color to compliment the beautiful cover design
Should not have
• Too much busy-ness in the image or the presentation.

```html
<!DOCTYPE html>
<html lang="en">
<head>
<meta charset="utf-8">
<title>Marcus Hale — Book Ad</title>
<link href="https://fonts.googleapis.com/css2?family=Poppins:wght@400;500;700&family=Tinos:wght@400;700&family=Archivo+Black&display=swap" rel="stylesheet">
<style>
  :root {
    --stage: #d6d6d6;
    --paper: #ffffff;
    --paper-tint: #f3f3f4;
    --ink: #1d1d1f;
    --navy: #0d2a9c;
    --royal: #0a44c4;
    --royal-deep: #0630a8;
    --pink: #f5076d;
    --pink-soft: #e0357a;
    --cover-deep: #12248f;
    --cover-mid: #2a63d6;
    --cover-light: #4fb3e8;
    --white: #ffffff;
  }
  * { margin: 0; padding: 0; box-sizing: border-box; }
  html, body { width: 1200px; height: 1200px; overflow: hidden; background: var(--stage); }

  .ad {
    position: absolute;
    left: 93px; top: 49px;
    width: 1448px; height: 1574px;
    transform: scale(0.7);
    transform-origin: top left;
    background: linear-gradient(135deg, var(--paper) 0%, var(--paper-tint) 100%);
    overflow: hidden;
    font-family: "Poppins", sans-serif;
  }
  .ad__shapes { position: absolute; inset: 0; width: 1448px; height: 1574px; }

  .publisher {
    position: absolute; left: 74px; top: 170px; width: 440px;
    display: flex; flex-direction: column; align-items: center; gap: 34px;
  }
  .publisher__dot {
    width: 150px; height: 150px; border-radius: 50%;
    background: var(--navy);
  }
  .publisher__name {
    font-family: "Poppins", sans-serif; font-weight: 500;
    font-size: 40px; line-height: 1; color: var(--ink);
  }

  .quote__text { position: absolute; font-size: 28px; line-height: 37.5px; font-weight: 400; }
  .quote--light .quote__text { left: 118px; top: 590px; width: 525px; color: var(--ink); }
  .quote--dark .quote__text { left: 123px; top: 1206px; width: 495px; color: var(--white); }

  .byline { position: absolute; font-family: "Tinos", serif; }
  .byline__name { font-weight: 700; font-size: 27px; line-height: 36px; }
  .byline__role { font-size: 27px; line-height: 36px; }
  .quote--light .byline { left: 118px; top: 838px; }
  .quote--light .byline__name { color: var(--navy); }
  .quote--light .byline__role { color: var(--pink-soft); }
  .quote--dark .byline { left: 128px; top: 1414px; color: var(--white); }

  .book { position: absolute; left: 702px; top: 110px; width: 676px; height: 1040px; }
  .book__pages {
    position: absolute; left: 600px; top: 14px; width: 70px; height: 1010px;
    background: linear-gradient(90deg, #e9e9ec, #ffffff 40%, var(--cover-deep) 85%);
    box-shadow: 8px 14px 30px rgba(0,0,0,.25);
  }
  .book__cover {
    position: absolute; left: 0; top: 0; width: 618px; height: 1040px;
    background: radial-gradient(circle at 55% 40%, var(--cover-light) 0%, var(--cover-mid) 40%, var(--cover-deep) 100%);
    box-shadow: 0 18px 40px rgba(0,0,0,.3);
  }
  .book__art {
    position: absolute; left: 150px; top: 400px; width: 420px; height: 620px;
    border-radius: 44% 44% 8% 8%;
    background: linear-gradient(160deg, #8a4fc4 0%, #3e6fd6 50%, #1c3c9e 100%);
    opacity: .8;
  }
  .book__title { position: absolute; left: 40px; top: 125px; font-family: "Archivo Black", sans-serif; color: var(--navy); }
  .book__title span { display: inline-block; background: var(--white); padding: 0 10px; line-height: 1.05; }
  .book__title .t1 { font-size: 38px; margin-left: 40px; }
  .book__title .t2 { font-size: 50px; margin-left: 16px; display: block; width: max-content; }
  .book__title .t3 { font-size: 38px; margin-left: 290px; display: block; width: max-content; }
  .book__title .t4 { font-size: 50px; display: block; width: max-content; }
  .book__author {
    position: absolute; left: 62px; top: 870px;
    font-family: "Archivo Black", sans-serif; font-size: 54px; letter-spacing: 6px; color: var(--white);
  }

  .buy-now {
    position: absolute; left: 953px; top: 1377px; width: 355px; height: 103px;
    border: 4px solid var(--white); border-radius: 52px;
    background: linear-gradient(180deg, #ff2d86, var(--pink) 60%, #d6005c);
    color: var(--white); font-weight: 700; font-size: 56px;
    display: flex; align-items: center; justify-content: center; text-decoration: none;
  }
</style>
</head>
<body>
<main class="ad">
  <svg class="ad__shapes" viewBox="0 0 1448 1574" aria-hidden="true">
    <defs>
      <linearGradient id="blueBand" x1="0" y1="0" x2="1" y2="1">
        <stop offset="0" stop-color="#0a50d6"/>
        <stop offset="1" stop-color="#0630a8"/>
      </linearGradient>
    </defs>
    <polygon points="0,937 433,1057 0,1159" fill="#f5076d"/>
    <polygon points="0,1159 1448,817 1448,1574 0,1574" fill="url(#blueBand)"/>
    <polygon points="480,1060 1448,1330 1448,817" fill="#0a56dc" opacity=".5"/>
    <!-- quote frame, light -->
    <path d="M108,572 H86 a12,12 0 0 0 -12,12 V788 a12,12 0 0 0 12,12 H102" fill="none" stroke="#0d2a9c" stroke-width="3"/>
    <path d="M180,572 H651 a12,12 0 0 1 12,12 V788 a12,12 0 0 1 -12,12 H476" fill="none" stroke="#e0357a" stroke-width="3"/>
    <text x="118" y="623" font-family="Poppins, sans-serif" font-weight="700" font-size="110" fill="#e0357a">“</text>
    <text x="414" y="867" font-family="Poppins, sans-serif" font-weight="700" font-size="110" fill="#0d2a9c">”</text>
    <!-- quote frame, dark -->
    <path d="M108,1184 H86 a12,12 0 0 0 -12,12 V1368 a12,12 0 0 0 12,12 H104" fill="none" stroke="#ffffff" stroke-width="3"/>
    <path d="M180,1184 H613 a12,12 0 0 1 12,12 V1368 a12,12 0 0 1 -12,12 H368" fill="none" stroke="#ffffff" stroke-width="3"/>
    <text x="118" y="1241" font-family="Poppins, sans-serif" font-weight="700" font-size="110" fill="#ffffff">“</text>
    <text x="308" y="1446" font-family="Poppins, sans-serif" font-weight="700" font-size="110" fill="#ffffff">”</text>
  </svg>

  <header class="publisher">
    <span class="publisher__dot" aria-hidden="true"></span>
    <p class="publisher__name">Northfield Books</p>
  </header>

  <section class="quote quote--light">
    <p class="quote__text">Marcus Hale’s writing has an underlying, yet profound sadness to it. IT is powerful in his work and key and keys into the inherit loneliness that all human beings experience at one time or another.</p>
    <div class="byline">
      <p class="byline__name">Dorian Welles</p>
      <p class="byline__role">Actor and Stage Director</p>
    </div>
  </section>

  <section class="quote quote--dark">
    <p class="quote__text">Marcus provokes us to look more carefully at systems of race and power and our participation in them in ways that linger long after the backout.</p>
    <div class="byline">
      <p class="byline__name">Nora Lindqvist</p>
      <p class="byline__role">Artistic Director, Bright Hall Stage</p>
    </div>
  </section>

  <figure class="book">
    <div class="book__pages"></div>
    <div class="book__cover">
      <div class="book__art" role="img" aria-label="Colourful mosaic-style portrait illustration of the author inside a glowing blue sphere"></div>
      <h2 class="book__title">
        <span class="t1">a few</span>
        <span class="t2">BRIEF SCENES</span>
        <span class="t3">to</span>
        <span class="t4">MEND THE WORLD</span>
      </h2>
      <p class="book__author">MARCUS HALE</p>
    </div>
  </figure>

  <a class="buy-now" href="#">Buy Now</a>
</main>
</body>
</html>
```